Business card design needed

I need a business card that sets my business apart from big gyms and intimidating personal trainers. My personal training business focuses on outdoor and client in-home training, in an environment that is both enjoyable and sustainable for the client.
I train males and females, however a large proportion of my clientelle are female, so I would like the card to lean towards females, but still have a bit of masculine appeal about it.
My business colours are a deep sky blue and lightish red/orange (as seen in logo)

Contact Information for Business Card

Bright Path Fitness Coach
Move well, feel strong, live bright!
Benedict Harlow- Health and Fitness Professional
Sessions held across Kestrel Vale and the Northbrook suburbs
0498315260
benedictharlowpt@quillmail.com.au

Requirements
Must have
• - Mobile number must stand out
- The 'Sessions held across Kestrel Vale and the Northbrook suburbs' must be clear and easy to read (different colour maybe?)

```html
<!DOCTYPE html>
<html lang="en">
<head>
<meta charset="utf-8">
<title>Bright Path Fitness Coach – Business Card</title>
<link rel="stylesheet" href="https://fonts.googleapis.com/css2?family=Open+Sans:wght@400;600;700&display=swap">
<style>
  :root {
    --sky-blue: #1f86c8;
    --coral: #ee5a2a;
    --card-white: #ffffff;
    --backdrop: #e6e8eb;
    --text-blue: #1f7fc0;
  }
  * { box-sizing: border-box; margin: 0; padding: 0; }
  html, body { width: 1200px; height: 900px; overflow: hidden; }
  body {
    background: var(--backdrop);
    font-family: "Open Sans", Arial, sans-serif;
    display: flex;
    flex-direction: column;
    align-items: center;
    justify-content: center;
    gap: 56px;
  }
  .card {
    position: relative;
    width: 640px;
    height: 366px;
    background: var(--card-white);
    box-shadow: 0 6px 24px rgba(0,0,0,0.14);
    overflow: hidden;
  }
  .brand { display: flex; align-items: center; gap: 16px; }
  .brand-mark {
    flex: none;
    border-radius: 50%;
    background: var(--coral);
  }
  .brand-name {
    font-weight: 700;
    color: var(--sky-blue);
    line-height: 1.05;
    white-space: nowrap;
  }
  .tagline {
    font-weight: 600;
    color: var(--coral);
    white-space: nowrap;
  }

  /* back side */
  .card-back { display: flex; align-items: center; justify-content: center; }
  .card-back .brand-mark { width: 96px; height: 96px; }
  .card-back .brand-name { font-size: 30px; }
  .card-back .tagline { font-size: 19px; margin-top: 6px; }

  /* front side */
  .card-front .brand { position: absolute; left: 40px; top: 28px; gap: 14px; }
  .card-front .brand-mark { width: 64px; height: 64px; }
  .card-front .brand-name { font-size: 22px; }
  .card-front .tagline { font-size: 14px; margin-top: 3px; }

  .holder { position: absolute; left: 40px; top: 122px; }
  .holder-name {
    font-size: 30px;
    font-weight: 400;
    letter-spacing: 0.5px;
    text-transform: uppercase;
    color: var(--text-blue);
  }
  .holder-role { font-size: 17px; color: var(--coral); margin-top: 2px; }
  .holder-area { font-size: 13px; color: var(--text-blue); margin-top: 10px; line-height: 1.35; }

  .bands { position: absolute; inset: 0; width: 640px; height: 366px; }

  .phone {
    position: absolute;
    right: 34px;
    top: 236px;
    display: flex;
    align-items: center;
    gap: 10px;
    font-size: 30px;
    color: var(--coral);
    letter-spacing: 1px;
  }
  .phone svg { width: 22px; height: 22px; }
  .email {
    position: absolute;
    right: 34px;
    top: 318px;
    font-size: 15px;
    color: var(--card-white);
  }
</style>
</head>
<body>

  <section class="card card-back" aria-label="Card back">
    <div class="brand">
      <span class="brand-mark"></span>
      <div>
        <div class="brand-name">Bright Path Fitness Coach</div>
        <div class="tagline">Move well, feel strong, live bright!</div>
      </div>
    </div>
  </section>

  <section class="card card-front" aria-label="Card front">
    <svg class="bands" viewBox="0 0 640 366" aria-hidden="true">
      <polygon points="0,272 246,272 288,366 0,366" fill="var(--coral)"/>
      <polygon points="300,292 640,292 640,366 334,366" fill="var(--sky-blue)"/>
    </svg>

    <div class="brand">
      <span class="brand-mark"></span>
      <div>
        <div class="brand-name">Bright Path Fitness Coach</div>
        <div class="tagline">Move well, feel strong, live bright!</div>
      </div>
    </div>

    <div class="holder">
      <h1 class="holder-name">Benedict Harlow</h1>
      <p class="holder-role">Health and Fitness Professional</p>
      <p class="holder-area">Sessions held across Kestrel Vale<br>and the Northbrook suburbs</p>
    </div>

    <div class="phone">
      <svg viewBox="0 0 24 24" aria-hidden="true">
        <circle cx="12" cy="12" r="11" fill="none" stroke="var(--sky-blue)" stroke-width="2"/>
        <path d="M8.5 6.5c.5-.4 1.2-.3 1.5.2l1.1 1.8c.3.5.2 1.1-.2 1.4l-.8.6c.5 1.3 1.6 2.5 2.9 3.1l.6-.8c.3-.4.9-.5 1.4-.2l1.8 1.1c.5.3.6 1 .2 1.5l-.8.9c-.6.6-1.5.8-2.3.5-3-1.2-5.3-3.5-6.4-6.5-.3-.8-.1-1.7.5-2.3z" fill="var(--sky-blue)"/>
      </svg>
      <span>0498 315 260</span>
    </div>
    <div class="email">benedictharlowpt@quillmail.com.au</div>
  </section>

</body>
</html>
```